PPT :The Art Market in a changing world

Nr of Slides :19

To do
As I have no PDF Converter from PDF to PPT

1 All slides needs to be put in the LANDSCAPE format(horizontal)
2 I need to be able to change every picture /title (so no PDF)
3 Style & Color =Basic is red and white see slide 1
4 Every Title must be in a Red Block & White Letters
5 I need to be able to change every picture text in order to be able to update

-Slide 5 from the PDF : date 2016 needs to be 2018
-Slide 8. from the PDF :date 17 should be 2018
-Slide 9. from the PDF :date 2015 should be 2018

-Update by adding the latest related info

Target Market(s)

Art Professionals
Showing the power off the Mobile Phone /Computer /Platforms as a tool for the new art economy
Therefore I added some pictures of mobile phones ..

Font styles to use
Sans Serif

Colors
ec1f27
0255a3
ffffff

Requirements
Must have
• Attached files have the shade/tone of red I'd like you to use in the design.
• I need to be able to update every part of the slide (Title,date, picture,graph)
• Mention on the last slide my social media /logo plus account
• Vimeo. Lucien Hodamar
• LinkedIn: Lucien Hodamar
• Twitter: HodamarLucien
Nice to have
• Possibility to insert a video (Vimeo)

```html
<!DOCTYPE html>
<html lang="en">
<head>
<meta charset="utf-8">
<title>The Art Market in a Changing World – Slide Deck</title>
<link href="https://fonts.googleapis.com/css2?family=Teko:wght@400;500&family=Raleway:wght@300;400&family=Open+Sans:wght@400;700&display=swap" rel="stylesheet">
<style>
  :root{
    --red:#ec1f27;
    --deep-red:#c8141b;
    --ink:#2b2b2b;
    --charcoal:#3a3a3a;
    --white:#ffffff;
    --stage-top:#f3f3f3;
    --stage-bottom:#d9d9d9;
  }
  *{margin:0;padding:0;box-sizing:border-box}
  html,body{width:912px;height:1200px;overflow:hidden}
  body{position:relative;background:var(--stage-bottom);font-family:"Raleway",sans-serif;color:var(--ink)}
  .hero-stage{position:absolute;left:0;top:0;width:912px;height:612px;background:var(--stage-top)}
  .slide{
    --u:calc(var(--w) / 517);
    position:absolute;width:var(--w);height:calc(var(--w) * 290 / 517);
    background:var(--white);overflow:hidden;box-shadow:0 6px 14px rgba(0,0,0,.18);
  }
  .slide--hero{--w:640px;left:136px;top:126px}
  .slide--a{--w:413px;left:37px;top:656px}
  .slide--b{--w:413px;left:468px;top:656px}
  .slide--c{--w:413px;left:37px;top:926px}
  .slide--d{--w:413px;left:468px;top:926px}
  .slide-frame{position:absolute;inset:0;width:100%;height:100%}
  .abs{position:absolute}
  .logo-box{left:calc(16*var(--u));top:calc(22*var(--u));width:calc(100*var(--u));height:calc(24*var(--u));
    border:calc(1.2*var(--u)) solid var(--ink);color:var(--red);font-family:"Open Sans",sans-serif;
    font-size:calc(15*var(--u));display:flex;align-items:center;justify-content:center;line-height:1}
  .headline{right:calc(14*var(--u));font-family:"Teko",sans-serif;font-weight:500;line-height:1;text-align:right;white-space:nowrap}
  .headline--red{top:calc(74*var(--u));font-size:calc(29*var(--u));color:var(--red)}
  .headline--dark{top:calc(107*var(--u));font-size:calc(29*var(--u));color:var(--ink)}
  .headline--white{top:calc(160*var(--u));font-size:calc(31*var(--u));color:var(--white)}
  .subhead{right:calc(14*var(--u));top:calc(192*var(--u));font-size:calc(13*var(--u));letter-spacing:calc(6*var(--u));color:var(--white);line-height:1}
  .event-name{left:0;right:0;top:calc(228*var(--u));text-align:center;font-weight:300;font-size:calc(24*var(--u));color:var(--ink);line-height:1}
  .site-url{left:0;right:0;top:calc(276*var(--u));display:flex;justify-content:center;align-items:center;gap:calc(6*var(--u));
    font-family:"Open Sans",sans-serif;font-size:calc(5.5*var(--u));color:var(--white);letter-spacing:calc(.6*var(--u));line-height:1}
  .site-url::before,.site-url::after{content:"";width:calc(60*var(--u));height:calc(.6*var(--u));background:var(--white)}
  .page-no{right:calc(14*var(--u));top:calc(279*var(--u));font-family:"Open Sans",sans-serif;font-weight:700;font-size:calc(5*var(--u));color:var(--ink);line-height:1}
  .photo--market{left:0;top:calc(35*var(--u));width:100%;height:calc(140*var(--u));background:linear-gradient(90deg,#2b3c58 0%,#1d2f4e 35%,#1e3a66 70%,#2a4a7a 100%)}
  .quote{left:calc(10*var(--u));right:calc(10*var(--u));top:calc(195*var(--u));text-align:center;font-size:calc(12.5*var(--u));line-height:1.25;color:var(--ink)}
  .quote-author{left:0;right:0;top:calc(238*var(--u));display:flex;justify-content:center;align-items:center;gap:calc(5*var(--u));
    font-family:"Open Sans",sans-serif;font-size:calc(7*var(--u));color:var(--ink);line-height:1}
  .quote-author::before,.quote-author::after{content:"";width:calc(14*var(--u));height:calc(.7*var(--u));background:var(--ink)}
  .gallery-photo{left:calc(72*var(--u));width:calc(255*var(--u));height:calc(100*var(--u));background:linear-gradient(90deg,#d9d2c8,#8a8780 45%,#cfcac2)}
  .gallery-photo--one{top:calc(37*var(--u))}
  .gallery-photo--two{top:calc(152*var(--u));background:linear-gradient(90deg,#efece6,#c9c1a9 50%,#8fae9e)}
  .caption-box{left:calc(327*var(--u));width:calc(125*var(--u));height:calc(100*var(--u));background:var(--red);color:var(--white);
    display:flex;flex-direction:column;align-items:center;justify-content:center;text-align:center;font-size:calc(7.5*var(--u));line-height:1.25}
  .caption-box--one{top:calc(37*var(--u))}
  .caption-box--two{top:calc(152*var(--u))}
  .caption-box strong{font-weight:400;font-size:calc(9*var(--u))}
  .agenda-title{left:calc(15*var(--u));top:calc(45*var(--u));font-size:calc(11.5*var(--u));font-weight:400;color:var(--ink);line-height:1}
  .agenda{left:calc(22*var(--u));top:calc(80*var(--u));list-style:none}
  .agenda li{position:absolute;left:0;display:flex;align-items:flex-start;gap:calc(7*var(--u));white-space:nowrap;
    font-family:"Open Sans",sans-serif;font-weight:700;font-size:calc(5.8*var(--u));color:var(--red);line-height:1.3}
  .agenda .num{flex:none;width:calc(11*var(--u));height:calc(11*var(--u));border-radius:50%;background:var(--red);color:var(--white);
    display:flex;align-items:center;justify-content:center;font-size:calc(5.5*var(--u));border:calc(1*var(--u)) solid #f6b4b6}
  .agenda .txt{padding-top:calc(2*var(--u))}
  .team-figure{left:calc(270*var(--u));top:calc(88*var(--u));width:calc(235*var(--u));height:calc(160*var(--u));
    background:linear-gradient(180deg,#3a3a3a,#111);border-radius:calc(3*var(--u))}
</style>
</head>
<body>
<div class="hero-stage"></div>

<section class="slide slide--hero">
  <svg class="slide-frame" viewBox="0 0 517 290" preserveAspectRatio="none" aria-hidden="true">
    <polygon points="205,0 517,0 517,12 217,12" fill="var(--red)"/>
    <polygon points="178,0 185,0 197,12 190,12" fill="var(--red)"/>
    <polygon points="188,0 192,0 204,12 200,12" fill="var(--ink)"/>
    <polygon points="0,68 312,68 324,88 0,88" fill="var(--red)"/>
    <polygon points="312,68 348,68 412,152 376,152" fill="var(--red)"/>
    <polygon points="258,88 290,88 326,150 290,212 258,212 294,150" fill="var(--red)"/>
    <polygon points="330,152 517,152 517,212 294,212" fill="var(--charcoal)"/>
    <polygon points="40,268 490,268 508,290 58,290" fill="var(--red)"/>
    <polygon points="0,262 4,262 32,290 28,290" fill="var(--ink)"/>
    <polygon points="0,270 4,270 24,290 20,290" fill="var(--red)"/>
    <polygon points="494,268 498,268 520,290 516,290" fill="var(--ink)"/>
  </svg>
  <svg class="slide-frame" viewBox="0 0 517 290" preserveAspectRatio="none" role="img" aria-label="Photo: wooden house and coin stacks with growing seedlings">
    <defs><linearGradient id="heroPhoto" x1="0" y1="0" x2="1" y2="1"><stop offset="0" stop-color="#5f8d3c"/><stop offset=".6" stop-color="#a7b46a"/><stop offset="1" stop-color="#c4a26a"/></linearGradient></defs>
    <polygon points="0,88 250,88 285,150 250,212 0,212" fill="url(#heroPhoto)"/>
  </svg>
  <div class="abs logo-box">LOGO HERE</div>
  <div class="abs headline headline--red">THE NEW ART</div>
  <div class="abs headline headline--dark">ECONOMY</div>
  <div class="abs headline headline--white">AUCTION HOUSES</div>
  <div class="abs subhead">DISRUPTED</div>
  <div class="abs event-name">GATHERING WEEK ART INSTITUTE</div>
  <div class="abs site-url">www.newarteconomy.net</div>
</section>

<section class="slide slide--a">
  <svg class="slide-frame" viewBox="0 0 517 290" preserveAspectRatio="none" aria-hidden="true">
    <polygon points="205,0 517,0 517,12 217,12" fill="var(--red)"/>
    <polygon points="178,0 185,0 197,12 190,12" fill="var(--red)"/>
    <polygon points="188,0 192,0 204,12 200,12" fill="var(--ink)"/>
    <polygon points="0,68 312,68 324,88 0,88" fill="var(--red)"/>
    <polygon points="312,68 348,68 412,152 376,152" fill="var(--red)"/>
    <polygon points="258,88 290,88 326,150 290,212 258,212 294,150" fill="var(--red)"/>
    <polygon points="330,152 517,152 517,212 294,212" fill="var(--charcoal)"/>
    <polygon points="40,268 490,268 508,290 58,290" fill="var(--red)"/>
    <polygon points="0,262 4,262 32,290 28,290" fill="var(--ink)"/>
    <polygon points="0,270 4,270 24,290 20,290" fill="var(--red)"/>
    <polygon points="494,268 498,268 520,290 516,290" fill="var(--ink)"/>
  </svg>
  <svg class="slide-frame" viewBox="0 0 517 290" preserveAspectRatio="none" role="img" aria-label="Photo: wooden house and coin stacks with growing seedlings">
    <defs><linearGradient id="titlePhoto" x1="0" y1="0" x2="1" y2="1"><stop offset="0" stop-color="#5f8d3c"/><stop offset=".6" stop-color="#a7b46a"/><stop offset="1" stop-color="#c4a26a"/></linearGradient></defs>
    <polygon points="0,88 250,88 285,150 250,212 0,212" fill="url(#titlePhoto)"/>
  </svg>
  <div class="abs logo-box">LOGO HERE</div>
  <div class="abs headline headline--red">THE NEW ART</div>
  <div class="abs headline headline--dark">ECONOMY</div>
  <div class="abs headline headline--white">AUCTION HOUSES</div>
  <div class="abs subhead">DISRUPTED</div>
  <div class="abs event-name">GATHERING WEEK ART INSTITUTE</div>
  <div class="abs site-url">www.newarteconomy.net</div>
</section>

<section class="slide slide--b">
  <svg class="slide-frame" viewBox="0 0 517 290" preserveAspectRatio="none" aria-hidden="true">
    <polygon points="40,0 517,0 517,12 52,12" fill="var(--red)"/>
    <polygon points="18,0 25,0 37,12 30,12" fill="var(--red)"/>
    <polygon points="28,0 32,0 44,12 40,12" fill="var(--ink)"/>
    <polygon points="40,268 460,268 478,290 58,290" fill="var(--red)"/>
    <polygon points="0,262 4,262 32,290 28,290" fill="var(--ink)"/>
    <polygon points="0,270 4,270 24,290 20,290" fill="var(--red)"/>
    <polygon points="464,268 468,268 490,290 486,290" fill="var(--ink)"/>
  </svg>
  <div class="abs photo--market" role="img" aria-label="Photo: businessman using a tablet in front of a stock market chart"></div>
  <p class="abs quote">CIVILIZATIONS ARE NOT REMEMBERED BY THEIR BUSINESS PEOPLE, BANKERS, OR LAWYERS. THEY ARE REMEMBERED BY THEIR ARTS.</p>
  <div class="abs quote-author">ARLEN MOSS</div>
  <div class="abs site-url">www.newarteconomy.net</div>
  <div class="abs page-no">01</div>
</section>

<section class="slide slide--c">
  <svg class="slide-frame" viewBox="0 0 517 290" preserveAspectRatio="none" aria-hidden="true">
    <polygon points="40,0 517,0 517,12 52,12" fill="var(--red)"/>
    <polygon points="18,0 25,0 37,12 30,12" fill="var(--red)"/>
    <polygon points="28,0 32,0 44,12 40,12" fill="var(--ink)"/>
    <polygon points="40,268 460,268 478,290 58,290" fill="var(--red)"/>
    <polygon points="0,262 4,262 32,290 28,290" fill="var(--ink)"/>
    <polygon points="0,270 4,270 24,290 20,290" fill="var(--red)"/>
    <polygon points="464,268 468,268 490,290 486,290" fill="var(--ink)"/>
  </svg>
  <div class="abs gallery-photo gallery-photo--one" role="img" aria-label="Photo: visitors viewing artworks in a gallery"></div>
  <div class="abs caption-box caption-box--one"><span>AUCTIONS TO INTERNET</span><strong>THE ART</strong></div>
  <div class="abs gallery-photo gallery-photo--two" role="img" aria-label="Photo: woman contemplating colourful paintings"></div>
  <div class="abs caption-box caption-box--two"><span>MARKET IN A</span><span>CHANGING WORLD</span></div>
  <div class="abs site-url">www.newarteconomy.net</div>
  <div class="abs page-no">02</div>
</section>

<section class="slide slide--d">
  <svg class="slide-frame" viewBox="0 0 517 290" preserveAspectRatio="none" aria-hidden="true">
    <polygon points="40,0 517,0 517,12 52,12" fill="var(--red)"/>
    <polygon points="18,0 25,0 37,12 30,12" fill="var(--red)"/>
    <polygon points="28,0 32,0 44,12 40,12" fill="var(--ink)"/>
    <polygon points="40,268 460,268 478,290 58,290" fill="var(--red)"/>
    <polygon points="0,262 4,262 32,290 28,290" fill="var(--ink)"/>
    <polygon points="0,270 4,270 24,290 20,290" fill="var(--red)"/>
    <polygon points="464,268 468,268 490,290 486,290" fill="var(--ink)"/>
  </svg>
  <h2 class="abs agenda-title">AUCTIONS TO INTERNET : THE ART MARKET IN A CHANGING WORLD</h2>
  <ol class="abs agenda">
    <li style="top:calc(0*var(--u))"><span class="num">1</span><span class="txt">INTRODUCTION</span></li>
    <li style="top:calc(23*var(--u))"><span class="num">2</span><span class="txt">CONTEXT - A TABLE OF TWO AUCTION HOUSES</span></li>
    <li style="top:calc(48*var(--u))"><span class="num">3</span><span class="txt">INTERNET &amp; GLOBALISATION :<br>REVOLUTION IN THE DYNAMIC OF THE ART MARKET</span></li>
    <li style="top:calc(83*var(--u))"><span class="num">4</span><span class="txt">THE AUCTION HOUSES DISRUPTED</span></li>
    <li style="top:calc(106*var(--u))"><span class="num">5</span><span class="txt">BENEFITS FOR THE PRIVATE COLLECTOR?</span></li>
    <li style="top:calc(130*var(--u))"><span class="num">6</span><span class="txt">CONCLUSION</span></li>
  </ol>
  <div class="abs team-figure" role="img" aria-label="Illustration: silhouettes of five business people"></div>
  <div class="abs site-url">www.newarteconomy.net</div>
  <div class="abs page-no">03</div>
</section>
</body>
</html>
```